Wix Website design for my therapy business - Willowmere Group

I have started designing a Wix site and have a good idea of what I want.
I have set up the pages, created some design ideas, and inputted the copy. I need someone fabulous to finish off the design aspects. I like working closely with the designers, I was an interior designer in an old career.
I would like the site to be funky but professional. My Wix skills are limited, and I just can't achieve the look I am wanting without having to spend a lot of time learning. If it's easier to start over, that's ok providing you use the same colours, font, images etc. I have included a screenshot of the home page below. I have another site I need to start as soon as we have finished this one.
I am looking for someone who is a good listener and is has design flare. I am easy to get along with and will respond quickly.
I would like to set up SEO and have help in the future.
Let me know if you are the right person for the job.
Target Market(s)
Please needing help with their mental health and for therapy.
Industry/Entity Type
Mental health
Font styles to use
Other font styles liked:
- Futura light
Requirements
Must have
- be easy to navigate and be simple yet stylish
Nice to have
- I have set up the basics of the site - nice to haves are already on the site
Should not have
- old fashioned large chunks of text.

```html
<!DOCTYPE html>
<html lang="en">
<head>
<meta charset="utf-8">
<title>Willowmere Group — Therapy</title>
<link href="https://fonts.googleapis.com/css2?family=Poppins:wght@300;400;500;600;700;800&display=swap" rel="stylesheet">
<style>
:root{
  --brown:#9a7d62;
  --brown-mid:#ad9279;
  --brown-light:#c2b0a0;
  --cream:#f7efe6;
  --mist:#f3f4f1;
  --ink:#2b2b2b;
  --text:#555;
  --line:#d9d2cb;
  --white:#fff;
}
*{margin:0;padding:0;box-sizing:border-box}
html,body{width:1200px;height:3857px;overflow:hidden}
body{position:relative;font-family:'Poppins',sans-serif;background:var(--white);color:var(--ink)}
.abs{position:absolute}
.site-logo{left:0;width:1200px;top:34px;text-align:center;font-size:40px;font-weight:500;color:var(--brown);letter-spacing:1px}
.nav{top:117px;left:0;width:1200px;height:56px;border-top:1px solid var(--line);border-bottom:1px solid var(--line)}
.nav ul{list-style:none;display:flex;justify-content:center;gap:34px;padding-top:15px;font-size:14px}
.nav li.active{color:var(--brown);border-bottom:2px solid var(--brown);padding-bottom:4px}
.hero{top:173px;left:0;width:1200px;height:622px}
.hero-title{left:127px;top:322px;color:var(--white);font-weight:800;line-height:.9}
.hero-title small{display:block;font-size:36px}
.hero-title span{display:block;font-size:74px}
.btn{background:var(--brown);color:var(--white);font-weight:600;font-size:16px;border-radius:5px;display:flex;align-items:center;justify-content:center}
.section-title{left:0;width:1200px;text-align:center;color:var(--brown);font-weight:700;font-size:39px}
.section-lead{left:0;width:1200px;text-align:center;font-size:15px;line-height:22px;color:var(--text)}
.card{top:1015px;width:304px;height:300px;border-radius:90px 10px 10px 10px;color:var(--white);text-align:center}
.card svg{margin-top:36px}
.card h3{font-size:20px;font-weight:600;margin-top:28px}
.card p{font-size:14px;line-height:18px;margin:18px 26px 0;font-weight:300}
.feature-title{left:129px;top:1590px;width:400px;color:var(--brown);font-weight:700;font-size:36px;line-height:41px}
.feature-text{left:126px;top:1740px;width:400px;font-size:15px;line-height:22.5px;color:var(--text)}
.photo{border-radius:18px}
.frame{left:166px;top:2312px;width:464px;height:463px;background:var(--white);border-radius:26px;box-shadow:0 4px 18px rgba(0,0,0,.08)}
.what-title{left:674px;top:2355px;color:var(--brown);font-weight:700;font-size:34px}
.what-text{left:674px;top:2420px;width:400px;font-size:15px;line-height:22.5px;color:var(--text)}
.service{left:673px;width:310px;font-size:24px;color:var(--ink)}
.service-rule{left:674px;width:308px;height:1px;background:#b8b8b8}
.field{border:1px solid #cfc7c0;font-size:14px;color:#666;padding:12px 12px;display:flex;align-items:flex-start;gap:6px;background:var(--white)}
.footer-h{color:var(--white);font-weight:700;font-size:18px}
.footer-link{color:var(--white);font-size:14px;line-height:24.7px}
.footer-logo{left:150px;top:3610px;width:240px;color:var(--white);font-weight:500;font-size:34px;line-height:40px}
.icon-box{width:34px;height:38px;border:2px solid var(--white);border-radius:6px;display:flex;align-items:center;justify-content:center}
</style>
</head>
<body>

<div class="abs site-logo">Willowmere Group</div>
<nav class="abs nav"><ul>
  <li class="active">Home</li><li>About Us</li><li>EMDR</li><li>Addictions</li><li>Betrayal Trauma</li><li>PTSD</li><li>Program List</li><li>Resources</li><li>Blog</li><li>Contact Us</li>
</ul></nav>

<!-- Hero -->
<svg class="abs hero" viewBox="0 0 1200 622" role="img" aria-label="Photo of a woman with a backpack raising her arms before a mountain landscape">
  <defs>
    <linearGradient id="heroSky" x1="0" y1="0" x2="1" y2="1">
      <stop offset="0" stop-color="#5a6a66"/><stop offset=".45" stop-color="#8e9b96"/><stop offset="1" stop-color="#3f4c45"/>
    </linearGradient>
  </defs>
  <path d="M0 0H1200V580C1100 630 900 640 700 560 560 500 340 500 0 545Z" fill="url(#heroSky)"/>
  <path d="M0 545C180 470 420 470 590 540 420 560 180 570 0 545Z" fill="var(--brown-light)"/>
  <path d="M0 545C200 520 420 525 590 540 460 560 250 580 0 545Z" fill="var(--brown)" opacity=".9"/>
</svg>
<div class="abs hero-title"><small>THE</small><span>Willowmere</span><span>Group</span></div>
<div class="abs btn" style="left:129px;top:507px;width:229px;height:53px">Make An Appointment</div>

<!-- Welcome -->
<div class="abs section-title" style="top:860px">Welcome to the Willowmere Group</div>
<div class="abs section-lead" style="top:927px">Lorem ipsum dolor sit amet, consectetur adipiscing elit, sed do eiusmod tempor incididunt<br>ut labore et dolore magna aliqua. Quis ipsum suspendisse ultrices gravida.</div>

<div class="abs card" style="left:129px;background:var(--brown)">
  <svg width="72" height="100" viewBox="0 0 72 100" fill="none" stroke="#fff" stroke-width="2.5"><circle cx="36" cy="28" r="20"/><path d="M6 98V78c0-12 12-20 30-20s30 8 30 20v20"/></svg>
  <h3>Individual Therapy</h3>
  <p>Lorem ipsum dolor sit amet, conse ctetur adipiscing elit, sed do eiusmod tempor incid.</p>
</div>
<div class="abs card" style="left:448px;background:var(--brown-mid)">
  <svg width="90" height="100" viewBox="0 0 90 100" fill="none" stroke="#fff" stroke-width="2.5"><path d="M45 16c-4-6-12-2-8 4l8 7 8-7c4-6-4-10-8-4z"/><circle cx="24" cy="52" r="16"/><circle cx="66" cy="52" r="16"/><path d="M2 98c0-18 10-26 22-26s22 8 22 26M44 98c0-18 10-26 22-26s22 8 22 26"/></svg>
  <h3>Couples Therapy</h3>
  <p>Lorem ipsum dolor sit amet, conse ctetur adipiscing elit, sed do eiusmod tempor incid.</p>
</div>
<div class="abs card" style="left:769px;background:var(--brown-light)">
  <svg width="90" height="100" viewBox="0 0 90 100" fill="none" stroke="#fff" stroke-width="2.5"><circle cx="24" cy="30" r="16"/><circle cx="66" cy="30" r="16"/><circle cx="45" cy="62" r="11"/><path d="M2 98V66c0-10 10-16 22-16M88 98V66c0-10-10-16-22-16M28 98c0-14 8-20 17-20s17 6 17 20"/></svg>
  <h3>Family Therapy</h3>
  <p>Lorem ipsum dolor sit amet, conse ctetur adipiscing elit, sed do eiusmod tempor incid.</p>
</div>

<!-- Feature band -->
<svg class="abs" style="left:0;top:1410px" width="1200" height="760" viewBox="0 0 1200 760">
  <defs><linearGradient id="band" x1="0" y1="0" x2="0" y2="1"><stop offset="0" stop-color="var(--cream)"/><stop offset="1" stop-color="#fdfbf8"/></linearGradient></defs>
  <path d="M0 103C250 -10 600 -30 900 20 1050 45 1150 90 1200 110V700C1000 660 700 650 420 680 250 700 100 690 0 690Z" fill="url(#band)"/>
  <path d="M0 690C150 660 300 680 420 680 700 650 1000 660 1200 700V760H0Z" fill="var(--mist)"/>
</svg>
<div class="abs feature-title">Lorem ipsum dolor sit amet&nbsp; consectetur lor adipis cing elit</div>
<div class="abs feature-text">Lorem ipsum dolor sit amet, consectetur adipiscing elit, sed do eiusmod tempor incididunt ut labore et dolore magna aliqua. Quis ipsum suspendisstrices gravida. Risus commodo viverra maecenas accumsan lacus vel facilisis.</div>
<div class="abs btn" style="left:127px;top:1884px;width:230px;height:53px">Make An Appointment</div>
<div class="abs photo" role="img" aria-label="Photo of a distressed woman being comforted during a session" style="left:562px;top:1627px;width:324px;height:374px;background:linear-gradient(135deg,#b9b3ab,#6e7c92 60%,#3d4a66)"></div>
<div class="abs" role="img" aria-label="Photo of a smiling family on a sofa" style="left:905px;top:1570px;width:193px;height:225px;border-radius:10px 80px 10px 10px;background:linear-gradient(160deg,#d8cfc2,#8a7a66)"></div>
<div class="abs" role="img" aria-label="Photo of a sad woman sitting hugging her knees" style="left:918px;top:1834px;width:206px;height:177px;border-radius:10px 10px 60px 10px;background:linear-gradient(160deg,#7b7a78,#3d4450)"></div>

<!-- What we do -->
<div class="abs" style="left:0;top:2170px;width:1200px;height:718px;background:var(--mist)"></div>
<div class="abs frame"></div>
<div class="abs" role="img" aria-label="Photo of a physiotherapist assisting a man exercising on a mat" style="left:178px;top:2324px;width:440px;height:439px;border-radius:18px;background:linear-gradient(160deg,#e7e4de,#b8aa98 60%,#8c7e72)"></div>
<div class="abs" style="left:168px;top:2301px;width:108px;height:108px;border-radius:50%;background:var(--brown)"></div>
<div class="abs what-title">What We Do</div>
<div class="abs what-text">Lorem ipsum dolor sit amet, consectetur adipiscing elit, sed do eiusmod tempor incididunt ut labore et dolore magna aliqua. amet, consectetur adipiscing elit, sed do eiusmod tempor.</div>
<div class="abs service" style="top:2533px">EMDR</div>
<div class="abs service-rule" style="top:2582px"></div>
<div class="abs service" style="top:2588px">Addictions</div>
<div class="abs service-rule" style="top:2634px"></div>
<div class="abs service" style="top:2643px">Betrayal Trauma</div>
<div class="abs service-rule" style="top:2692px"></div>
<div class="abs service" style="top:2698px">PTSD</div>

<!-- Contact -->
<div class="abs section-title" style="top:2965px">Contact Us</div>
<div class="abs section-lead" style="top:3029px">Lorem ipsum dolor sit amet, consectetur adipiscing elit, sed do eiusmod tempor incididunt<br>ut labore et dolore magna aliqua. amet, consectetur adipiscing eli sed do eiusm.</div>
<div class="abs field" style="left:200px;top:3107px;width:257px;height:46px">&#9786; Name:</div>
<div class="abs field" style="left:472px;top:3107px;width:258px;height:46px">&#9993; Email:</div>
<div class="abs field" style="left:745px;top:3107px;width:256px;height:46px">&#9742; Phone:</div>
<div class="abs field" style="left:200px;top:3163px;width:801px;height:156px">&#128172; Message:</div>
<div class="abs btn" style="left:526px;top:3285px;width:148px;height:53px">Submit Now</div>

<!-- Footer -->
<svg class="abs" style="left:0;top:3380px" width="1200" height="477" viewBox="0 0 1200 477">
  <path d="M0 18C120 70 260 100 420 85 650 60 850 -20 1050 5 1130 15 1180 30 1200 40V477H0Z" fill="var(--brown)"/>
  <path d="M165 78C260 50 440 52 520 62 400 90 260 98 165 78Z" fill="#e8e2dc"/>
</svg>
<div class="abs footer-logo">Willowmere<br>Group</div>
<div class="abs footer-h" style="left:443px;top:3565px">Menu</div>
<div class="abs" style="left:443px;top:3601px;width:64px;height:2px;background:var(--white)"></div>
<div class="abs footer-link" style="left:443px;top:3612px">Home<br>About Us<br>EMDR<br>Addictions<br>Betrayal Trauma</div>
<div class="abs footer-link" style="left:614px;top:3612px">PTSD<br>Program List<br>Resources<br>Blog<br>Contact Us</div>
<div class="abs footer-h" style="left:794px;top:3565px">Contact</div>
<div class="abs icon-box" style="left:794px;top:3619px"><svg width="18" height="18" viewBox="0 0 24 24" fill="#fff"><path d="M6.6 10.8a15 15 0 0 0 6.6 6.6l2.2-2.2a1 1 0 0 1 1-.25 11 11 0 0 0 3.6.6 1 1 0 0 1 1 1V20a1 1 0 0 1-1 1A17 17 0 0 1 3 4a1 1 0 0 1 1-1h3.5a1 1 0 0 1 1 1 11 11 0 0 0 .6 3.6 1 1 0 0 1-.25 1Z"/></svg></div>
<div class="abs footer-link" style="left:838px;top:3614px;line-height:18px">Phone:<br>(02) 5550 1234</div>
<div class="abs icon-box" style="left:794px;top:3670px"><svg width="18" height="14" viewBox="0 0 24 18" fill="#fff"><path d="M0 0h24v18H0Z M2 2l10 8 10-8" stroke="var(--brown)" stroke-width="2"/></svg></div>
<div class="abs footer-link" style="left:838px;top:3665px;line-height:18px">Email:<br>hello@willowmeregroup.example</div>
<div class="abs" style="left:105px;top:3790px;width:990px;height:1px;background:rgba(255,255,255,.35)"></div>
<div class="abs" style="left:1031px;top:3769px;width:46px;height:46px;border:2px solid var(--white);border-radius:6px;background:var(--brown)"></div>
<div class="abs footer-link" style="left:0;width:1200px;text-align:center;top:3810px">Copyright © 2023 The Willowmere Group. All Rights Reserved.</div>

</body>
</html>
```